Brochure Design Template

We need a template design so we can add and change content as required.

The size is A4 Landscape (297mm X 210mm) divided into three individual DL sections (99mm X 210mm) that have their own individual color or look. This give us the option to print as DL or have three separate services offered on on brochure.

So who are we. We are a photographic service that in Australia that offers service from commercial photography, photography training, photographic studio hire as well as a photo booth.
Our website is brivlane.net.

We are after ideas that are modern and colorful and fits the look of our logo.. Please feel free to put questions or ideas to us..
Thanks kindly..

Target Market(s)

weddings and commerical businesses

Industry/Entity Type

Landscape

Requirements
Must have
• The size is A4 Landscape (297mm X 210mm) divided into three individual DL sections (99mm X 210mm) that have their own individual color or look. This give us the option to print as DL or have three separate services offered on on brochure.

Template is for use in Adobe indesign

```html
<!DOCTYPE html>
<html lang="en">
<head>
<meta charset="utf-8">
<title>Brivlane Photographic Services – Tri-fold Brochure</title>
<link href="https://fonts.googleapis.com/css2?family=Source+Sans+3:wght@300;400&display=swap" rel="stylesheet">
<style>
  :root {
    --canvas-bg: #e9e4dc;
    --sheet-bg: #0b0b0b;
    --accent-red: #e3242b;
    --stripe-grey: #c9c9c9;
    --body-text: #e6e6e6;
    --muted-text: #cfcfcf;
  }
  * { box-sizing: border-box; margin: 0; padding: 0; }
  html, body {
    width: 1200px; height: 892px; overflow: hidden;
    background: var(--canvas-bg);
    font-family: "Source Sans 3", sans-serif;
  }
  .brochure {
    position: absolute; left: 50px; top: 57px;
    width: 1100px; height: 778px;
    background: var(--sheet-bg);
    box-shadow: 0 6px 18px rgba(0,0,0,.35);
    display: flex;
  }
  .stripe {
    position: absolute; left: 0; width: 100%; height: 15px; z-index: 2;
    background: repeating-linear-gradient(90deg,
      var(--accent-red) 0 45px, var(--stripe-grey) 45px 91px);
  }
  .stripe--top { top: 248px; }
  .stripe--bottom { bottom: 0; height: 16px; }
  .panel {
    position: relative; width: 366.67px; height: 100%;
  }
  .panel__photos { display: flex; height: 248px; position: relative; }
  .photo { flex: 1; height: 100%; }
  .photo--booth { flex: 0 0 175px; background: linear-gradient(160deg, #9c9690, #3a3532 55%, #6b5a55); }
  .photo--reader { background: linear-gradient(150deg, #1b1b1b, #b56a2c 55%, #d9b684 85%, #3a2a20); }
  .photo--field { background: linear-gradient(180deg, #8e9a8d 0%, #6c7a66 35%, #2c4a78 65%, #1e2430 100%); }
  .photo--portrait { background: linear-gradient(120deg, #141414 0%, #3a2a26 35%, #d9a893 60%, #b52a33 85%, #5a1a1a); }
  .photo-tag {
    position: absolute; right: 22px; bottom: 6px;
    color: var(--accent-red); font-weight: 300; font-size: 21px; line-height: 24px;
  }
  .panel--hire .photo-tag { right: auto; left: 34px; }
  .panel__title {
    position: absolute; top: 290px; left: 0; width: 100%;
    text-align: center; color: var(--accent-red);
    font-weight: 300; font-size: 37px; line-height: 44px; letter-spacing: -.5px;
  }
  .panel__copy {
    position: absolute; top: 357px; left: 28px; right: 28px;
    color: var(--body-text); font-size: 11.3px; line-height: 16.2px;
    text-align: justify;
  }
  .panel--hire .panel__copy { text-align: left; }
  .panel__copy p + p { margin-top: 9px; }
  .panel--hire .panel__copy p + p { margin-top: 30px; }
  .brand {
    display: flex; align-items: center; gap: 10px;
    color: #ffffff; font-weight: 400; letter-spacing: 1px;
  }
  .brand__dot { width: 14px; height: 14px; border-radius: 50%; background: var(--accent-red); }
  .panel__sign { position: absolute; left: 0; width: 100%; }
  .phone { color: var(--muted-text); font-weight: 300; }

  .panel--hire .panel__sign { top: 650px; padding-left: 78px; }
  .panel--hire .brand { font-size: 26px; line-height: 32px; }
  .panel--hire .phone { font-size: 33px; line-height: 40px; letter-spacing: 1px; margin-top: 6px; }

  .panel--training .panel__sign { top: 628px; text-align: center; }
  .panel--training .brand { justify-content: center; font-size: 20px; line-height: 26px; }
  .contact { color: var(--muted-text); font-weight: 300; }
  .contact__mail { font-size: 14px; line-height: 18px; letter-spacing: 3px; margin-top: 38px; }
  .contact__web { font-size: 17px; line-height: 22px; letter-spacing: 4px; margin-top: 4px; }

  .panel--commercial .panel__sign { top: 668px; padding-left: 42px; }
  .panel--commercial .brand { font-size: 36px; line-height: 42px; }
  .panel--commercial .phone { font-size: 19px; line-height: 24px; letter-spacing: 1.5px; margin: 4px 0 0 190px; }
</style>
</head>
<body>
<main class="brochure">
  <div class="stripe stripe--top"></div>
  <div class="stripe stripe--bottom"></div>

  <section class="panel panel--hire">
    <div class="panel__photos">
      <div class="photo photo--booth" role="img" aria-label="Photo of a girl in a novelty hat sitting inside a photo booth"></div>
      <div class="photo photo--reader" role="img" aria-label="Photo of a woman in glasses browsing a photo album at a desk"></div>
      <span class="photo-tag">photography</span>
    </div>
    <h2 class="panel__title">HIRE &amp; BOOTH</h2>
    <div class="panel__copy">
      <p>The photo booth is the perfect addition for your wedding, party or corporate event providing you with a timeless keepsake. The photo booth will provide you with not one, but two photo strips 5 x 15cm in colour or black &amp; white with three to four photos on each – we can even personalize each strip to incorporate your wedding date, special message or corporate logo. But hold on – the fun does not stop there – using our multi-function screen you can choose your own borders, hairstyle, hat and so much more with the whole process taking less than a minute.</p>
      <p>Brivlane has a unique fully equipped studio space that can be hired. The space is ideal for portraits that can be captured with a white seamless background or one of other eight backdrops available for use.</p>
    </div>
    <div class="panel__sign">
      <div class="brand"><span class="brand__dot"></span>BRIVLANE</div>
      <div class="phone">0491570156</div>
    </div>
  </section>

  <section class="panel panel--training">
    <div class="panel__photos">
      <div class="photo photo--field" role="img" aria-label="Photo of two photographers shooting with cameras in front of mountains"></div>
      <span class="photo-tag">photography</span>
    </div>
    <h2 class="panel__title">TRAINING</h2>
    <div class="panel__copy">
      <p>Enrol in the most comprehensive digital photography course designed for beginners by pro photographers!</p>
      <p>These SLR photography courses are designed for those who are new to the digital SLR photography world and want to get professional looking images from their new camera.<br>Qualified Professional Teaching NPIA Photographer for 18 hours tuition. Workbook with detailed notes. Light refreshments available throughout the evening (includes water, tea &amp; coffee plus supper). Studio equipment for demonstrations. Two, 3 hour photographic field trips with comprehensive demonstrations. Framed image of one of your images selected by the teaching staff. Final field trip finished with a beer, wine or soft drink.</p>
    </div>
    <div class="panel__sign">
      <div class="brand"><span class="brand__dot"></span>BRIVLANE</div>
      <div class="contact contact__mail">mailto:mail@brivlane.net</div>
      <div class="contact contact__web">www.brivlane.net</div>
    </div>
  </section>

  <section class="panel panel--commercial">
    <div class="panel__photos">
      <div class="photo photo--portrait" role="img" aria-label="Close-up beauty portrait with red lips on a dark background"></div>
      <span class="photo-tag">photography</span>
    </div>
    <h2 class="panel__title">COMMERCIAL</h2>
    <div class="panel__copy">
      <p>Brivlane Photographic Services provides unique event, corporate, portraiture, architecture and landscape photography services across New South Wales, Australia. They specialise in training, photographic tours and also have a studio space and photobooth available to hire...</p>
      <p>Brivlane Photographic Services specialises in producing high-quality images and will ensure that all our shoots are relaxed, professional and trouble-free. We provide a secure and easy-to-use online store for purchasing professional print and digital products that you will treasure forever. Contact us to discuss your requirements and let us show you how we can make your event extra special.</p>
    </div>
    <div class="panel__sign">
      <div class="brand"><span class="brand__dot"></span>BRIVLANE</div>
      <div class="phone">0491570156</div>
    </div>
  </section>
</main>
</body>
</html>
```